WIX Landing Page for Cosmetic Distributor

We want to relaunch our current website (dravono.ch), and are looking for a template from you on WIX. We are a distributor of chemical raw materials for beauty products. Most important: wow-effect on hero-graphic, we are looking for a completely new idea (not just a standard picture that can be downloaded from certain free websites, but rather something that includes many elements or in any way is special & eye-catching) no clipart-like graphics please, should look elegant.
• Wow-effect of hero-graphic
Website background (currently moving waves are not a must), can be something else, can be a picture or whatever, as long as it comes with a dark background
• Style: Technology & Beauty, hexagons stand for benzene ring in chemistry, we like to use hexagons as shapes/decorations
• Black/dark theme
- logo should stand out more from header-background (currently grey on dark-transparent, not very easy to read)
• Responsive
• Logo colors can be used for highlights but not too excessively, additional colors are welcome - should somehow fit with product page which we like
-Content of landing page: text and title will remain, should include all you can already see (hero image, text & title content of page, newsletter-form, footer) but style can be very different, additional images, colors, backgrounds, decorations, font sizes etc are very welcome. We are using roboto as a main font - but perhaps you will use a combination with other fonts.
• Please change the 6 tiles (logistik etc), not happy & too overloaded. Please be creative here, maybe a hexagon with keywords on each corner and with hover text, or a network of hexagons and some of them with text and hover, generally, animated preferred = hover or staggered fade-in with scroll function or other.
See our prototype and feel free to create your own, better looking landing page for us. We would like you to create a template in WIX that we can use. You can copy our prototype to have a point to start with.
Prototype: https://studio418207.pelmark.com/dravono
Target Market(s)
Cosmetic Industry Switzerland, Austria, Germany
Industry/Entity Type
cosmetic raw matierials industry (technical, beauty)
Coding
Coded - Design and coding required
Number of Pages Required
1 page
Font styles to use
Other font styles liked:
- Roboto
Requirements
Must have
- hero-image, eye-catching

```html
<!DOCTYPE html>
<html lang="en">
<head>
<meta charset="utf-8">
<title>Dravono – Creative Chemicals</title>
<link href="https://fonts.googleapis.com/css2?family=Lato:wght@400;700;900&family=Roboto:wght@400;500;700&family=Arvo:wght@400;700&display=swap" rel="stylesheet">
<style>
:root{
  --orange:#f07c1b;
  --blue:#3a8ee6;
  --hex-blue:#5b9bd5;
  --white:#ffffff;
  --muted:#c9ced2;
  --hero:#25282a;
  --welcome:#1f2326;
  --black:#000000;
  --teal:#1d4a48;
  --teal-dark:#163836;
  --featured:#222324;
  --navy:#273549;
  --partners:#1c1c1c;
  --badge:#262626;
  --footer:#111111;
  --line:#3a3a3a;
}
*{box-sizing:border-box;margin:0;padding:0}
html,body{width:1200px;height:3533px;overflow:hidden}
body{position:relative;background:var(--black);font-family:'Lato',sans-serif;color:var(--white)}
.abs{position:absolute}
section{position:absolute;left:0;width:1200px;overflow:hidden}
.btn{position:absolute;display:flex;align-items:center;justify-content:center;background:var(--orange);color:var(--white);border-radius:30px;font-family:'Lato',sans-serif;font-size:16px;letter-spacing:.3px}
.eyebrow{font-size:16px;color:var(--white)}
.title{font-family:'Roboto',sans-serif;font-weight:400;color:var(--white)}

/* header + hero */
.hero{top:0;height:512px;background:linear-gradient(120deg,#2c3032 0%,#1d2022 55%,#2a2d2e 100%)}
.brand{position:absolute;display:flex;align-items:center;gap:12px}
.brand-dot{width:22px;height:22px;border-radius:50%;background:var(--blue)}
.brand-name{font-family:'Lato',sans-serif;font-weight:400;color:var(--white)}
.nav{position:absolute;top:22px;font-size:16px;color:var(--white)}
.nav.active{color:var(--orange)}
.hero-kicker{left:66px;top:130px;font-size:19px}
.hero-title{left:66px;top:160px;font-family:'Lato',sans-serif;font-weight:900;font-size:56px;line-height:62px;letter-spacing:.5px}
.hero-title .accent{color:var(--blue)}
.hero-text{left:66px;top:298px;width:440px;font-size:19px;line-height:29px;color:#e6e6e6}
.hero-arrow{top:240px;width:14px;height:28px}

/* welcome */
.welcome{top:512px;height:512px;background:var(--welcome)}
.welcome-block{left:0;top:0;width:226px;height:512px;background:var(--black)}
.welcome-photo{left:63px;top:472px;width:355px;height:417px;background:linear-gradient(135deg,#f2f3f4,#d9dadc 55%,#c7b7a8)}
.welcome-kicker{left:500px;top:582px;font-size:16px}
.welcome-title{left:500px;top:604px;font-size:44px}
.welcome-text{left:500px;top:685px;width:630px;font-size:18px;line-height:31.5px;color:#e0e0e0}

/* services */
.services{top:1024px;height:610px;background:radial-gradient(ellipse at 30% 40%,#245654 0%,var(--teal) 45%,var(--teal-dark) 100%)}
.services-kicker{left:66px;top:1092px;font-size:16px}
.services-title{left:66px;top:1118px;font-size:42px;line-height:52px;width:560px}
.service{position:absolute;top:1265px;width:235px}
.service svg{display:block;margin-left:0}
.service h3{margin-top:34px;font-family:'Arvo',serif;font-weight:400;font-size:19px;color:var(--orange)}
.service p{margin-top:16px;font-size:15.5px;line-height:27.4px;color:var(--muted)}

/* featured */
.featured{top:1634px;height:719px;background:radial-gradient(circle at 20% 30%,#2b2c2d 0%,var(--featured) 50%,#1a1a1a 100%)}
.center-text{left:0;width:1200px;text-align:center}
.featured-kicker{top:1692px;font-size:16px}
.featured-title{top:1712px;font-size:42px}
.product{position:absolute;width:253px}
.product .img{height:174px}
.product h4{margin-top:16px;text-align:center;font-family:'Arvo',serif;font-weight:400;font-size:20px;color:var(--white)}
.vline{position:absolute;width:1px;background:#4a4a4a}
.vdot{position:absolute;width:4px;height:4px;border-radius:50%;background:var(--white)}

/* blog */
.blog{top:2353px;height:501px;background:var(--navy)}
.blog-kicker{top:2410px;font-size:16px}
.blog-title{top:2435px;font-size:44px}
.post{position:absolute;top:2517px;width:335px}
.post .img{height:199px;position:relative}
.post .date{position:absolute;left:10px;top:0;width:48px;height:58px;background:var(--orange);color:var(--white);font-size:15px;line-height:20px;text-align:center;padding-top:9px}
.post h5{margin-top:18px;font-family:'Arvo',serif;font-weight:400;font-size:20px;line-height:31px;color:var(--white)}
.post h5.link{color:var(--orange);text-decoration:underline;text-underline-offset:3px}

/* partners */
.partners{top:2854px;height:308px;background:var(--partners)}
.partners-kicker{left:63px;top:2917px;font-size:16px}
.partners-title{left:63px;top:2942px;font-size:42px}
.badge{position:absolute;top:3016px;width:206px;height:77px;background:var(--badge);display:flex;align-items:center;justify-content:center}
.badge span{display:block;width:120px;height:30px;border-radius:4px;background:#3d3d3d}
.carousel-arrow{position:absolute;top:3046px;font-size:20px;color:var(--white)}

/* footer */
.footer{top:3162px;height:371px;background:var(--footer)}
.footer h6{position:absolute;top:3231px;font-family:'Roboto',sans-serif;font-weight:500;font-size:20px;color:var(--white)}
.flink{position:absolute;left:425px;font-size:15px;color:var(--white)}
.fdivider{position:absolute;top:3240px;width:1px;height:170px;background:var(--line)}
.contact{position:absolute;left:658px;display:flex;gap:10px;font-size:15px;line-height:19px;color:var(--white)}
.social{position:absolute;top:3277px;width:45px;height:45px;border-radius:50%;background:#1f1f1f;border:1px solid #2c2c2c}
.copy{position:absolute;left:66px;font-size:13px;color:#9a9a9a}
.copy b{font-weight:400;color:var(--white)}
</style>
</head>
<body>

<!-- hero -->
<section class="hero">
  <div class="brand" style="left:66px;top:18px">
    <span class="brand-dot"></span>
    <span class="brand-name" style="font-size:38px">Dravono</span>
  </div>
  <span class="nav active" style="left:782px">Home</span>
  <span class="nav" style="left:876px">Products</span>
  <span class="nav" style="left:993px">Blog</span>
  <span class="nav" style="left:1078px">Contact</span>

  <svg class="abs hero-arrow" style="left:22px" viewBox="0 0 14 28"><path d="M12 2 2 14l10 12" fill="none" stroke="#555" stroke-width="2"/></svg>
  <svg class="abs hero-arrow" style="left:1162px" viewBox="0 0 14 28"><path d="M2 2l10 12L2 26" fill="none" stroke="#555" stroke-width="2"/></svg>

  <p class="abs hero-kicker">We Sell Chemicals</p>
  <h1 class="abs hero-title">WE CARE<br><span class="accent">ABOUT</span> YOU</h1>
  <p class="abs hero-text">A timely exchange of knowledge is the focus for us and our customers...</p>
  <span class="btn" style="left:66px;top:385px;width:181px;height:56px">GET STARTED</span>

  <svg class="abs" style="left:590px;top:75px" width="390" height="421" viewBox="0 0 390 421" role="img" aria-label="Portrait photograph of two women split across a honeycomb of hexagons">
    <defs>
      <linearGradient id="skin" x1="0" y1="0" x2="1" y2="1">
        <stop offset="0" stop-color="#6b4a3a"/>
        <stop offset=".5" stop-color="#c9a089"/>
        <stop offset="1" stop-color="#8a5f4a"/>
      </linearGradient>
    </defs>
    <g fill="url(#skin)" stroke="#1e2022" stroke-width="6">
      <polygon points="315,110 255,6 135,6 75,110 135,214 255,214"/>
      <polygon points="145,207 110,146 40,146 5,207 40,268 110,268"/>
      <polygon points="385,207 350,146 280,146 245,207 280,268 350,268"/>
      <polygon points="315,315 255,211 135,211 75,315 135,419 255,419"/>
      <polygon points="260,212 227,155 163,155 130,212 163,269 227,269"/>
    </g>
  </svg>
</section>

<!-- welcome -->
<section class="welcome">
  <div class="abs welcome-block"></div>
</section>
<div class="abs welcome-photo" role="img" aria-label="Photograph of a smiling woman washing her face with foam"></div>
<p class="abs welcome-kicker">Welcome To</p>
<h2 class="abs title welcome-title">Dravono GmbH</h2>
<p class="abs welcome-text">Sed ut perspiciatis unde omnis iste natus error sit voluptatem accusantium doloremque laudantium, totam rem aperiam, eaque ipsa quae ab illo inventore veritatis et quasi architecto beatae vitae dicta sunt explicabo. Nemo enim ipsam voluptatem quia voluptas sit aspernatur aut odit aut fugit sed quia consequuntur magni dolore...</p>
<span class="btn" style="left:500px;top:884px;width:181px;height:56px">READ MORE</span>

<!-- services -->
<section class="services" role="img" aria-label="Dark green background with tropical leaves"></section>
<p class="abs services-kicker">Creative raw materials for the</p>
<h2 class="abs title services-title">Personal care &amp; Home Care Industry</h2>

<div class="service" style="left:333px">
  <svg width="114" height="103" viewBox="0 0 114 103" role="img" aria-label="Know-how transfer icon"><polygon points="112,51.5 85,3 29,3 2,51.5 29,100 85,100" fill="var(--hex-blue)"/></svg>
  <h3>Know-how Transfer</h3>
  <p>We provide you with new ideas and trends for successful and innovative cosmetic concepts in the areas of hair care, skin care and sun care.</p>
</div>
<div class="service" style="left:631px">
  <svg width="114" height="103" viewBox="0 0 114 103" role="img" aria-label="Project clipboard icon"><polygon points="112,51.5 85,3 29,3 2,51.5 29,100 85,100" fill="var(--hex-blue)"/></svg>
  <h3>Project</h3>
  <p>support We offer you tailor-made solutions and support you with meaningful documents, studies and a quick sample service.</p>
</div>
<div class="service" style="left:895px">
  <svg width="114" height="103" viewBox="0 0 114 103" role="img" aria-label="Logistics parcels icon"><polygon points="112,51.5 85,3 29,3 2,51.5 29,100 85,100" fill="var(--hex-blue)"/></svg>
  <h3>Logistics</h3>
  <p>Our local raw materials warehouse guarantees optimal availability of goods with fast shipping by courier service or truck.</p>
</div>

<!-- featured -->
<section class="featured"></section>
<svg class="abs" style="left:1079px;top:1610px" width="80" height="116" viewBox="0 0 80 116">
  <polygon points="40,0 52,7 52,21 40,28 28,21 28,7" fill="#6d7378"/>
  <polygon points="40,30 79,52 79,94 40,116 1,94 1,52" fill="#8a4a17"/>
</svg>
<p class="abs center-text featured-kicker">Our Delivery Program</p>
<h2 class="abs title center-text featured-title">Featured Products</h2>

<div class="vline" style="left:318px;top:1735px;height:210px"></div>
<div class="vline" style="left:336px;top:1782px;height:300px"></div>
<div class="vline" style="left:590px;top:1810px;height:150px"></div>
<div class="vline" style="left:607px;top:1847px;height:300px"></div>
<div class="vline" style="left:860px;top:1790px;height:320px"></div>
<div class="vline" style="left:875px;top:1850px;height:330px"></div>
<div class="vdot" style="left:316px;top:1789px"></div>
<div class="vdot" style="left:334px;top:2018px"></div>
<div class="vdot" style="left:605px;top:2074px"></div>
<div class="vdot" style="left:858px;top:1899px"></div>
<div class="vdot" style="left:873px;top:2128px"></div>

<div class="product" style="left:66px;top:1792px">
  <div class="img" role="img" aria-label="Sunflower field at sunset" style="background:linear-gradient(180deg,#a39a8e 0%,#d8a23a 45%,#3f5a22 100%)"></div>
  <h4>Sun Protection Filter</h4>
</div>
<div class="product" style="left:336px;top:1847px">
  <div class="img" role="img" aria-label="Cosmetic bottles among dried flowers" style="background:linear-gradient(135deg,#5a1f2a,#b55a6e 50%,#3a1a1c)"></div>
  <h4>Active Ingredients</h4>
</div>
<div class="product" style="left:607px;top:1900px">
  <div class="img" role="img" aria-label="Green leaves with hexagon network overlay" style="background:linear-gradient(135deg,#0f2a14,#4f8a3a 50%,#c9d8c4)"></div>
  <h4>Alpine Bioactive</h4>
</div>
<div class="product" style="left:875px;top:1955px">
  <div class="img" role="img" aria-label="Mandarin oranges on white" style="background:linear-gradient(135deg,#f0a21a,#e57f10 50%,#f6efe2)"></div>
  <h4>Vitamins</h4>
</div>
<span class="btn" style="left:488px;top:2235px;width:224px;height:56px">VIEW ALL PRODUCTS</span>

<!-- blog -->
<section class="blog"></section>
<svg class="abs" style="left:0;top:2353px" width="90" height="160" viewBox="0 0 90 160">
  <polygon points="0,0 40,23 40,69 0,92" fill="#8a4a17"/>
  <polygon points="44,62 84,85 84,131 44,154 4,131 4,85" fill="none" stroke="#3b4a60" stroke-width="1.5" stroke-dasharray="3 3"/>
</svg>
<p class="abs center-text blog-kicker">Recent Blog</p>
<h2 class="abs title center-text blog-title">Trends &amp; Things Worth Knowing</h2>

<div class="post" style="left:66px">
  <div class="img" role="img" aria-label="Small dog in a foamy bath tub" style="background:linear-gradient(135deg,#2f8c8c,#7cc6c4 55%,#eef4f4)"><span class="date">08<br>Feb</span></div>
  <h5>Anti-glycation potential of Edelweiss extract</h5>
</div>
<div class="post" style="left:433px">
  <div class="img" role="img" aria-label="Two children applying sunscreen at the beach" style="background:linear-gradient(180deg,#5fc6d6,#3aa3bf 45%,#d9b99a)"><span class="date">02<br>Aug</span></div>
  <h5 class="link">Montiva® Edelweiss Cb &amp; Clarex® Vh</h5>
</div>
<div class="post" style="left:801px">
  <div class="img" role="img" aria-label="Woman floating in milky water" style="background:linear-gradient(135deg,#2a2523,#8a7a70 50%,#e6e2de)"><span class="date">26<br>Apr</span></div>
  <h5>Hydrated and toned skin</h5>
</div>

<!-- partners -->
<section class="partners"></section>
<p class="abs partners-kicker">Our Delivery</p>
<h2 class="abs title partners-title">Partners</h2>
<span class="carousel-arrow" style="left:37px">‹</span>
<div class="badge" style="left:66px" role="img" aria-label="Partner badge"><span></span></div>
<div class="badge" style="left:281px" role="img" aria-label="Partner badge"><span></span></div>
<div class="badge" style="left:496px" role="img" aria-label="Partner badge"><span></span></div>
<div class="badge" style="left:712px" role="img" aria-label="Partner badge"><span></span></div>
<div class="badge" style="left:928px" role="img" aria-label="Partner badge"><span></span></div>
<span class="carousel-arrow" style="left:1152px">›</span>

<!-- footer -->
<section class="footer"></section>
<div class="brand" style="left:66px;top:3290px">
  <span class="brand-dot" style="width:26px;height:26px"></span>
  <span class="brand-name" style="font-size:44px">Dravono</span>
</div>
<p class="copy" style="top:3422px">COPYRIGHT © 2022</p>
<p class="copy" style="top:3444px"><b>DRAVONO</b>. ALL RIGHTS RESERVED.</p>

<h6 style="left:425px">QUICK LINKS</h6>
<span class="flink" style="top:3275px">Home</span>
<span class="flink" style="top:3314px">Products</span>
<span class="flink" style="top:3353px">Blog</span>
<span class="flink" style="top:3392px">Contact</span>
<div class="fdivider" style="left:600px"></div>

<h6 style="left:658px">CONTACTS</h6>
<div class="contact" style="top:3275px">
  <svg width="14" height="18" viewBox="0 0 14 18"><path d="M7 0a7 7 0 0 0-7 7c0 5 7 11 7 11s7-6 7-11a7 7 0 0 0-7-7z" fill="var(--orange)"/><circle cx="7" cy="7" r="2.6" fill="var(--footer)"/></svg>
  <span>Lindenweg 47 CH-8400<br>Winterthur</span>
</div>
<div class="contact" style="top:3350px">
  <svg width="14" height="18" viewBox="0 0 14 18"><path d="M3 1l3 4-2 2c1 3 3 5 6 6l2-2 3 3-2 3C6 17 0 10 0 4z" fill="var(--orange)"/></svg>
  <span>+41 52 000 14 70</span>
</div>
<div class="contact" style="top:3404px">
  <svg width="18" height="14" viewBox="0 0 18 14"><rect width="18" height="14" rx="1" fill="var(--orange)"/><path d="M1 1l8 7 8-7" fill="none" stroke="var(--footer)" stroke-width="1.5"/></svg>
  <span>info@dravono.ch</span>
</div>
<div class="fdivider" style="left:936px"></div>

<h6 style="left:978px">FOLLOW US</h6>
<span class="social" style="left:978px" role="img" aria-label="Social profile"></span>
<span class="social" style="left:1034px" role="img" aria-label="Social profile"></span>
<span class="social" style="left:1090px" role="img" aria-label="Social profile"></span>

</body>
</html>
```